Accountants Stationary Package

Letter head, compliment slip, business card, report cover

Using selected logo which will be supplied when available design with compliment slip, letter head, business card and report cover. Some information to be amended and will be supplied at revision stage, design needs to resonate with chosen logo.

Update information 1 business card - my name is "Martin Kessler" post numerals are FCA , TITLE = Managing Director, (but maybe chartered accountant) is ok, my personal mobile is 0417 58 63 14 and personal email ids martin.k@kesslerledger.com,au, I like the tag line included " everybody ....succcess" Don't want professional liability logo but ok with the PQ and tallo logo I like the colours I like the blue back where it has a soft watermark finish 2. letterheads Need logos for tallo, PQ, professional standards Needs full company name and ABN NUMmber as - Kessler Ledger Pty Limited, ACN 748 206 513 Linked in ? I am also ok with initials instead of icons for phone, email, fax mobile, etc

Industry/Entity Type

Accounting

Requirements
Must have
• Kessler Ledger Pty Limited
• ABN 480591736
• Charted accountants
• Telephone 612 48350926
• Fax 612 4859 0417
• Po Box 6841, Tarrin, NSW, 2317
• Mobile 0417 586 314
• Address 42 Wenlock road, Tarrin, suite 8 Wenlock Central
• Mail@kesslerledger.com.au
• Website kesslerledger.com.au
• List of services;
• Tax and Accounting
• Business Development
• Superannuation and Financial Services

```html
<!DOCTYPE html>
<html lang="en">
<head>
<meta charset="utf-8">
<title>Kessler Ledger Stationery</title>
<link href="https://fonts.googleapis.com/css2?family=Open+Sans:wght@400;600&family=Arimo:wght@400;700&family=Dancing+Script:wght@600&display=swap" rel="stylesheet">
<style>
:root{
  --board:#636363;
  --ink:#000;
  --paper:#fff;
  --blue:#1ea0dc;
  --green:#8dc63f;
  --orange:#f15a29;
  --text:#333;
  --muted:#555;
}
*{margin:0;padding:0;box-sizing:border-box}
html,body{width:1189px;height:1200px;overflow:hidden}
body{background:var(--board);position:relative;font-family:"Open Sans",sans-serif;color:var(--text)}
.piece{position:absolute;overflow:hidden}
.brand{position:absolute;display:flex;align-items:center;gap:7px}
.brand-mark{background:var(--blue);flex:none}
.brand-text{display:flex;flex-direction:column;white-space:nowrap}
.brand-name{font-family:"Open Sans",sans-serif;font-weight:600;color:var(--blue);letter-spacing:.3px;line-height:1}
.brand-tag{color:var(--orange);letter-spacing:.4px;line-height:1;margin-top:3px;font-family:"Open Sans",sans-serif}
.stripe{position:absolute;left:0;right:0;bottom:0;display:flex}
.stripe span{display:block;height:100%}
.s-black{background:var(--ink);flex:0 0 60%}
.s-green{background:var(--green);flex:0 0 16.5%}
.s-orange{background:var(--orange);flex:0 0 15%}
.s-blue{background:var(--blue);flex:1}
.blue{color:var(--blue)}

/* report cover */
.cover{left:82px;top:194px;width:419px;height:542px;background:var(--ink)}
.cover .spine{position:absolute;left:12px;top:0;bottom:12px;width:2px;background:#222}
.cover .url{position:absolute;left:0;right:0;top:479px;text-align:center;font-size:7px;color:var(--blue)}
.cover .url::before,.cover .url::after{content:"";display:inline-block;width:30px;height:1px;background:var(--blue);vertical-align:middle;margin:0 12px}

/* letterhead */
.letter{left:518px;top:199px;width:419px;height:541px;background:var(--paper)}
.letter .divider{position:absolute;left:144px;top:35px;width:1px;height:445px;background:var(--blue)}
.letter .side{position:absolute;left:21px;top:92px;width:115px;font-size:6.4px;line-height:8.6px;color:var(--muted)}
.letter .side h3{font-weight:400;font-size:8px;line-height:8px;color:var(--blue);margin-bottom:5px}
.letter .side h4{font-weight:600;font-size:8.4px;color:var(--blue);margin:9px 0 2px}
.letter .side p{margin-bottom:7px}
.letter .side .lab{color:var(--blue)}
.letter .emblem{position:absolute;left:22px;top:388px;width:40px;height:40px;background:var(--blue)}
.letter .body{position:absolute;left:162px;top:38px;width:230px;font-family:"Arimo",sans-serif;font-size:6.6px;line-height:12.3px;color:#222}
.letter .to{line-height:8.4px;margin-bottom:30px}
.letter .to strong{font-size:7.6px;font-weight:400;display:block;margin-bottom:4px}
.letter .body p{margin-bottom:12px}
.letter .sign{font-family:"Dancing Script",cursive;font-size:26px;line-height:30px;color:#111;margin-top:-4px}
.letter .signer{font-size:7.4px;line-height:9px}
.letter .signer b{font-weight:700}

/* drives */
.drive{position:absolute;width:130px;height:52px;display:flex;box-shadow:2px 3px 4px rgba(0,0,0,.45)}
.drive .shell{flex:0 0 106px;display:flex;align-items:center;justify-content:center}
.drive .cap{flex:1;border-radius:0 3px 3px 0}
.drive .dot{width:24px;height:24px;background:var(--blue)}
.drive-dark{left:963px;top:587px}
.drive-dark .shell{background:var(--ink)}
.drive-dark .cap{background:linear-gradient(90deg,#cfcfcf,#fff)}
.drive-light{left:963px;top:687px}
.drive-light .shell{background:var(--paper)}
.drive-light .cap{background:linear-gradient(90deg,#111,#333)}

/* compliments slip */
.slip{left:82px;top:805px;width:364px;height:171px;background:var(--paper)}
.slip .fade{position:absolute;left:220px;top:0;right:0;bottom:10px;background:linear-gradient(90deg,#f2f6f9,#fafcfd)}
.slip .info{position:absolute;left:16px;top:80px;font-size:6.3px;line-height:7.6px;color:var(--muted)}
.slip .info h3{font-weight:400;font-size:7.6px;color:var(--blue);margin-bottom:1px}
.slip .info h4{font-weight:400;font-size:7.4px;color:var(--blue);margin:8px 0 3px}
.slip .addr{position:absolute;left:259px;top:122px;font-size:5.8px;line-height:7.4px;color:var(--muted)}
.slip .addr p+p{margin-top:7px}
.slip-label{position:absolute;left:82px;width:364px;top:992px;text-align:center;font-size:18px;color:#fff;letter-spacing:.4px}

/* business card */
.card-front{left:529px;top:823px;width:268px;height:153px;background:var(--paper)}
.card-front .abn{position:absolute;right:13px;top:18px;font-size:6.4px;color:var(--muted)}
.card-front .role{position:absolute;left:12px;right:13px;top:80px;font-size:9.4px;color:var(--muted);border-bottom:1px solid var(--blue);padding-bottom:1px}
.card-front .contact{position:absolute;left:12px;top:103px;font-size:6.6px;line-height:8.7px;color:var(--muted)}
.card-front .addr{position:absolute;right:13px;top:103px;font-size:6.6px;line-height:8.7px;color:var(--muted);text-align:right}
.card-front .addr p+p{margin-top:8px}
.card-back{left:827px;top:823px;width:268px;height:154px;background:var(--ink);color:#fff;text-align:center}
.card-back .glow{position:absolute;left:60px;top:0;width:150px;height:154px;background:linear-gradient(180deg,#10151c,#0b0d10)}
.card-back h3{position:relative;margin-top:24px;font-size:8.4px;font-weight:600;color:var(--blue)}
.card-back .services{position:relative;font-size:6.4px;line-height:8.6px;margin-top:6px}
.card-back .partners{position:relative;display:flex;justify-content:center;align-items:center;gap:16px;margin-top:15px}
.partner{display:flex;align-items:center;gap:4px;font-size:8px}
.partner-circle{width:30px;height:30px;border-radius:50%;background:var(--blue)}
.partner-square{width:18px;height:22px;background:#fff}
.card-back .web{position:relative;margin-top:17px;font-size:6.6px;font-weight:600}
</style>
</head>
<body>

<section class="piece cover" aria-label="Report cover">
  <div class="spine"></div>
  <div class="brand" style="left:110px;top:93px">
    <div class="brand-mark" style="width:50px;height:50px"></div>
    <div class="brand-text">
      <span class="brand-name" style="font-size:16px">KESSLER LEDGER</span>
      <span class="brand-tag" style="font-size:5.6px">every figure shapes your progress</span>
    </div>
  </div>
  <p class="url">kesslerledger.com.au</p>
</section>

<section class="piece letter" aria-label="Letterhead">
  <div class="brand" style="left:21px;top:42px">
    <div class="brand-mark" style="width:28px;height:28px"></div>
    <div class="brand-text">
      <span class="brand-name" style="font-size:8.4px">KESSLER LEDGER</span>
      <span class="brand-tag" style="font-size:3.6px;letter-spacing:.2px">every figure shapes your progress</span>
    </div>
  </div>
  <div class="side">
    <h3>Kessler Ledger Pty Limited</h3>
    <p>ABN 480591736</p>
    <h3 style="margin-top:12px">Charted accountants</h3>
    <p><span class="lab">T:</span> 612 48350926<br><span class="lab">F:</span> 612 4859 0417<br><span class="lab">M:</span> 0417 586 314<br><span class="lab">E:</span> Mail@kesslerledger.com.au</p>
    <p>42 Wenlock road, Tarrin<br>suite 8 Wenlock Central</p>
    <p>Po Box 6841, Tarrin, NSW, 2317</p>
    <h4>OUR SERVICES</h4>
    <p>-Tax and Accounting<br>-Business Development<br>-Superannuation and Financial Services</p>
    <p class="blue">kesslerledger.com.au</p>
  </div>
  <div class="emblem"></div>
  <div class="divider"></div>
  <div class="body">
    <div class="to"><strong>JOHN SMITH</strong>Street Name,City Name.<br>Zip Coad 0000</div>
    <p>Lorem Ipsum is simply dummy text of the printing and typesetting industry's standard dummy text ever since the 1500s, when an unknown printer scrambled it to make a type specimen book. It has survived not only electronic typesetting, remaining essentially unchanged. It was popularised with the release of Presset sheets containing Lorem Ipsum passages, and more recently like Folio PageBuilder including versions of Lorem Ipsum.</p>
    <p>It is a long established fact that a reader will be distracted by the readable content at its layout. The point of using Lorem Ipsum is that it has a more-or-less normal distribution, as opposed to using 'Content here, content here', making it look like readable English. Many desktop publishing packages and web page editors now use Lorem Ipsum as their default model text, and a search for 'lorem ipsum' will uncover many web sites still in their infancy. Various versions have evolved over the years, sometimes by accident, sometimes on purpose.</p>
    <p>Lorem Ipsum is simply dummy text of the printing and typesetting industry's standard dummy text ever since the 1500s, when an unknown printer scrambled it to make a type specimen book. It has survived not only electronic typesetting, remaining essentially unchanged. It was popularised with the release of Presset sheets containing Lorem Ipsum passages, and more recently like Folio PageBuilder including versions of Lorem Ipsum.</p>
    <p>It is a long established fact that a reader will be distracted by the readable content at its layout. The point of using Lorem Ipsum is that it has a more or less opposed</p>
    <p style="margin:0">Regards,</p>
    <div class="sign">John Doe</div>
    <div class="signer"><b>John Doe</b><br>General Maneger</div>
  </div>
  <div class="stripe" style="height:12px"><span class="s-black"></span><span class="s-green"></span><span class="s-orange"></span><span class="s-blue"></span></div>
</section>

<div class="drive drive-dark" aria-label="USB drive, dark"><div class="shell"><div class="dot"></div></div><div class="cap"></div></div>
<div class="drive drive-light" aria-label="USB drive, light"><div class="shell"><div class="dot"></div></div><div class="cap"></div></div>

<section class="piece slip" aria-label="Compliments slip">
  <div class="fade"></div>
  <div class="brand" style="left:16px;top:21px">
    <div class="brand-mark" style="width:33px;height:33px"></div>
    <div class="brand-text">
      <span class="brand-name" style="font-size:10px">KESSLER LEDGER</span>
      <span class="brand-tag" style="font-size:4px;letter-spacing:.2px">every figure shapes your progress</span>
    </div>
  </div>
  <div class="info">
    <h3>Kessler Ledger Pty Limited</h3>
    <p>ABN 480591736</p>
    <h4>Charted accountants</h4>
    <p><span class="blue">T:</span> 612 48350926<br><span class="blue">F:</span> 612 4859 0417<br><span class="blue">M:</span> 0417 586 314<br><span class="blue">E:</span> Mail@kesslerledger.com.au</p>
  </div>
  <div class="addr"><p>42 Wenlock road, Tarrin<br>suite 8 Wenlock Central</p><p>Po Box 6841, Tarrin, NSW, 2317</p></div>
  <div class="stripe" style="height:10px"><span class="s-black"></span><span class="s-green"></span><span class="s-orange"></span><span class="s-blue"></span></div>
</section>
<p class="slip-label">compliments slip</p>

<section class="piece card-front" aria-label="Business card front">
  <div class="brand" style="left:12px;top:15px">
    <div class="brand-mark" style="width:38px;height:38px"></div>
    <div class="brand-text">
      <span class="brand-name" style="font-size:11.5px">KESSLER LEDGER</span>
      <span class="brand-tag" style="font-size:4.4px;letter-spacing:.3px">every figure shapes your progress</span>
    </div>
  </div>
  <p class="abn">ABN 480591736</p>
  <p class="role">Charted accountants</p>
  <div class="contact"><span class="blue">T:</span> 612 48350926<br><span class="blue">F:</span> 612 4859 0417<br><span class="blue">M:</span> 0417 586 314<br><span class="blue">E:</span> Mail@kesslerledger.com.au</div>
  <div class="addr"><p>Po Box 6841, Tarrin, NSW, 2317</p><p>42 Wenlock road, Tarrin<br>suite 8 Wenlock Central</p></div>
  <div class="stripe" style="height:8px"><span class="s-black"></span><span class="s-green"></span><span class="s-orange"></span><span class="s-blue"></span></div>
</section>

<section class="piece card-back" aria-label="Business card back">
  <div class="glow"></div>
  <h3>OUR SERVICES</h3>
  <p class="services">Tax and Accounting<br>Business Development | Superannuation and Financial Services</p>
  <div class="partners">
    <div class="partner"><span class="partner-circle"></span>tallo</div>
    <div class="partner"><span class="partner-circle" style="width:16px;height:16px;background:var(--orange)"></span>PQ</div>
    <span class="partner-square" aria-label="Professional standards badge"></span>
  </div>
  <p class="web">www.<span class="blue">kesslerledger</span>.com.au</p>
</section>

</body>
</html>
```